KPV Construction we build lodges in Botswana

We need a Design Layout only with Categories where we can update each projects photos.... We have a web address and a host - kpv.construction

```html
<!DOCTYPE html>
<html lang="en">
<head>
<meta charset="utf-8">
<title>KPV Construction</title>
<link href="https://fonts.googleapis.com/css2?family=Lato:wght@400;700&family=Michroma&display=swap" rel="stylesheet">
<style>
:root{
  --blue:#1f74c4;
  --red:#f0303a;
  --ink:#1d1d1d;
  --body:#3a3a3a;
  --muted:#777;
  --light:#f6f6f6;
  --line:#dcdcdc;
  --footer:#232323;
  --white:#fff;
}
*{box-sizing:border-box;margin:0;padding:0}
html,body{width:1200px;height:3297px;overflow:hidden;background:var(--white)}
body{position:relative;font-family:"Lato",sans-serif;color:var(--body)}
.abs{position:absolute}
.display{font-family:"Michroma",sans-serif;color:var(--ink);letter-spacing:1px}
.btn{position:absolute;display:flex;align-items:center;justify-content:center;color:var(--white);font-size:14px;font-weight:700;border-radius:3px;background:var(--blue)}
.btn.red{background:var(--red)}

/* hero */
.hero{position:absolute;left:0;top:0;width:1200px;height:631px;background:linear-gradient(180deg,#c9dcef 0%,#e6eef3 30%,#7b5a3e 45%,#6a4a30 60%,#7f9b4a 72%,#5f8a36 100%)}
.menu-icon{left:121px;top:50px}
.logo{position:absolute;left:0;width:1200px;top:72px;text-align:center;font-weight:700;font-size:15px;color:var(--blue);letter-spacing:1px}
.hero-title{left:0;width:1200px;top:328px;text-align:center;font-size:31px;color:var(--white)}
.hero-sub{left:0;width:1200px;top:368px;text-align:center;font-size:14px;line-height:18px;color:var(--white);font-weight:700}

/* about */
.eyebrow{left:121px;top:730px;font-size:14px;color:var(--ink)}
.about-title{left:121px;top:752px;font-size:36px}
.about-rule{left:121px;top:801px;width:147px;height:3px;background:var(--blue)}
.about-text{left:121px;top:822px;width:440px;font-size:13.5px;line-height:17px;color:var(--ink)}
.about-text p+p{margin-top:12px}
.photo{position:absolute}

/* projects */
.projects{position:absolute;left:0;top:1220px;width:1200px;height:536px;display:grid;grid-template-columns:repeat(3,1fr);grid-template-rows:repeat(2,1fr);gap:2px;background:var(--white)}
.project{position:relative;display:flex;flex-direction:column;align-items:center;justify-content:center;color:var(--white);text-align:center}
.project h3{font-family:"Michroma",sans-serif;font-size:19px;font-weight:400;color:var(--white)}
.project.active{background:linear-gradient(#3a2a1e,#2a1d14)!important}
.project.active p{font-size:14px;font-weight:700;line-height:17px;margin-top:10px;width:260px}
.project.active .more{font-size:14px;font-weight:700;margin-top:10px}

/* blogs */
.blogs{position:absolute;left:0;top:1756px;width:1200px;height:545px;background:var(--light)}
.blogs-title{left:0;width:1200px;top:40px;text-align:center;font-size:31px}
.card{position:absolute;top:108px;width:290px}
.card .thumb{height:180px;position:relative}
.badge{position:absolute;left:0;top:16px;width:32px;background:var(--red);color:var(--white);font-size:11px;font-weight:700;line-height:11px;padding:3px 0 3px 4px}
.card h4{font-family:"Michroma",sans-serif;font-size:12px;font-weight:400;color:var(--ink);margin-top:12px;letter-spacing:.5px}
.meta{display:flex;font-size:13px;color:var(--ink);margin-top:8px;gap:8px;align-items:center}
.meta .stats{margin-left:auto;display:flex;gap:14px}
.card p{font-size:13px;line-height:17px;color:var(--muted);margin-top:10px}
.card .more{font-size:13px;color:var(--ink);margin-top:8px;display:flex;align-items:center;gap:4px}

/* contact */
.section-h{font-size:26px}
.contact-note{left:121px;top:2432px;width:370px;font-size:13px;line-height:17px;color:var(--ink)}
.field{position:absolute;left:121px;width:457px;height:42px;border:1px solid var(--line);font-size:13px;color:var(--muted);padding:12px 14px}
.map{left:611px;top:2433px;width:475px;height:453px;background:linear-gradient(135deg,#ececec,#dfe3e6);border:3px solid #f0f0f0}

/* footer */
.footer{position:absolute;left:0;top:2915px;width:1200px;height:322px;background:var(--footer);color:#d8d8d8;font-size:13px;line-height:24px}
.footer h5{position:absolute;top:78px;font-family:"Michroma",sans-serif;font-size:14px;font-weight:400;color:var(--white);letter-spacing:1px}
.footer ul{list-style:none}
.footer li{display:flex;align-items:center;gap:10px}
.sub-field{left:121px;top:224px;width:180px;height:34px;background:var(--white);color:#333;font-size:11px;padding:9px 14px;border-radius:3px 0 0 3px}
.sub-btn{left:301px;top:224px;width:42px;height:34px;background:var(--red);border-radius:0 3px 3px 0;display:flex;align-items:center;justify-content:center}
.bar{position:absolute;left:0;top:3237px;width:1200px;height:60px;background:var(--blue);color:var(--white);font-size:13px;font-weight:700}
</style>
</head>
<body>

<header class="hero" role="img" aria-label="Photo of a large log lodge with a green roof, stone garden terraces and lawn">
  <svg class="abs menu-icon" width="26" height="20" viewBox="0 0 26 20"><rect y="1" width="26" height="3" fill="#222"/><rect y="9" width="26" height="3" fill="#222"/><rect y="17" width="18" height="3" fill="#222"/></svg>
  <div class="logo">KPV CONSTRUCTION</div>
  <div class="btn" style="left:941px;top:48px;width:140px;height:36px">Contact us</div>
  <h1 class="abs display hero-title" style="font-weight:400">CONSTRUCTION COMPANY</h1>
  <p class="abs hero-sub">We are a Construction Company basedin the Okavango Delta<br>and specialize in Lodge building...</p>
  <div class="btn" style="left:455px;top:429px;width:138px;height:33px">Read More</div>
  <div class="btn red" style="left:609px;top:429px;width:138px;height:33px">Get Started</div>
</header>

<section>
  <p class="abs eyebrow">About us</p>
  <h2 class="abs display about-title" style="font-weight:400">WHO WE ARE</h2>
  <div class="abs about-rule"></div>
  <div class="abs about-text">
    <p>Lorem Ipsum is simply dummy text of the printing and typesetting industry. Lorem Ipsum has been the industry's standard dummy text ever since the 1500s,</p>
    <p>when an unknown printer took a galley of type and scrambled it to make a type specimen book. It has survived not only five centuries</p>
  </div>
  <div class="btn" style="left:121px;top:985px;width:139px;height:33px">Read More</div>
  <div class="photo" style="left:600px;top:708px;width:229px;height:182px;background:linear-gradient(#c7a584,#55604a)" role="img" aria-label="Photo of a modern lodge at dusk"></div>
  <div class="photo" style="left:849px;top:767px;width:228px;height:180px;background:linear-gradient(#4a3424,#8a5a2c)" role="img" aria-label="Photo of a lit lodge deck at night"></div>
  <div class="photo" style="left:600px;top:910px;width:229px;height:182px;background:linear-gradient(#5a3a20,#b07a38)" role="img" aria-label="Photo of a thatched lodge interior lit warmly"></div>
  <div class="photo" style="left:849px;top:969px;width:228px;height:185px;background:linear-gradient(#8a9aa8,#6b5a44)" role="img" aria-label="Photo of a lodge terrace overlooking the delta"></div>
</section>

<section class="projects">
  <div class="project" style="background:linear-gradient(#3b4036,#2a2420)" role="img" aria-label="Photo of a lodge among palm trees"><h3>PROJECT HEADING</h3></div>
  <div class="project active">
    <h3>PROJECT HEADING</h3>
    <p>Lorem Ipsum is simply dummy text of the printing and typesetting and in the Industry.</p>
    <div class="more">Read More..</div>
  </div>
  <div class="project" style="background:linear-gradient(#2e3236,#3d4a58)" role="img" aria-label="Photo of a lodge with a pool at dusk"><h3>PROJECT HEADING</h3></div>
  <div class="project" style="background:linear-gradient(#7a6c56,#4e5a3e)" role="img" aria-label="Photo of thatched lodge huts"><h3>PROJECT HEADING</h3></div>
  <div class="project" style="background:linear-gradient(#6f7a86,#3a4a4c)" role="img" aria-label="Photo of a lodge with an infinity pool"><h3>PROJECT HEADING</h3></div>
  <div class="project" style="background:linear-gradient(#5a2e1a,#3a2214)" role="img" aria-label="Photo of a wooden deck with dining tables"><h3>PROJECT HEADING</h3></div>
</section>

<section class="blogs">
  <h2 class="abs display blogs-title" style="font-weight:400">BLOGS</h2>

  <article class="card" style="left:121px">
    <div class="thumb" style="background:linear-gradient(#a88c6a,#6a4a2c)" role="img" aria-label="Photo of a lodge lounge with sofas"><div class="badge">20<br>Jan</div></div>
    <h4>BLOG TITLE HEADING</h4>
    <div class="meta"><span>▤ Jan 21, 2019</span><span class="stats"><span>◌20</span><span>♡ 12</span></span></div>
    <p>Lorem Ipsum is simply dummy text of the matter and typesetting in industry.</p>
    <div class="more">Read More <svg width="11" height="11" viewBox="0 0 11 11"><circle cx="5.5" cy="5.5" r="4.5" fill="none" stroke="#333"/><path d="M4.5 3.5l2 2-2 2" fill="none" stroke="#333"/></svg></div>
  </article>

  <article class="card" style="left:457px">
    <div class="thumb" style="background:linear-gradient(#c47a3a,#6a3e20)" role="img" aria-label="Photo of a lodge at sunset"><div class="badge">21<br>Jan</div></div>
    <h4>BLOG TITLE HEADING</h4>
    <div class="meta"><span>▤ Jan 22, 2019</span><span class="stats"><span>◌20</span><span>♡ 12</span></span></div>
    <p>Lorem Ipsum is simply dummy text of the matter and typesetting in industry.</p>
    <div class="more">Read More <svg width="11" height="11" viewBox="0 0 11 11"><circle cx="5.5" cy="5.5" r="4.5" fill="none" stroke="#333"/><path d="M4.5 3.5l2 2-2 2" fill="none" stroke="#333"/></svg></div>
  </article>

  <article class="card" style="left:791px">
    <div class="thumb" style="background:linear-gradient(#3a2a1c,#a06a30)" role="img" aria-label="Photo of a thatched lodge lit at night"><div class="badge">21<br>Jan</div></div>
    <h4>BLOG TITLE HEADING</h4>
    <div class="meta"><span>▤ April10, 2018</span><span class="stats"><span>◌20</span><span>♡12</span></span></div>
    <p>Lorem Ipsum is simply dummy text of the matter and typesetting in industry.</p>
    <div class="more">Read More <svg width="11" height="11" viewBox="0 0 11 11"><circle cx="5.5" cy="5.5" r="4.5" fill="none" stroke="#333"/><path d="M4.5 3.5l2 2-2 2" fill="none" stroke="#333"/></svg></div>
  </article>

  <div class="btn" style="left:523px;top:459px;width:156px;height:36px;font-size:16px;font-weight:400">View More</div>
</section>

<section>
  <h2 class="abs display section-h" style="left:121px;top:2386px;font-weight:400">QUICK CONTACT</h2>
  <p class="abs contact-note">Please fill out this quick contact form and someone will be in touch with you shortly</p>
  <div class="field" style="top:2488px">Name*</div>
  <div class="field" style="top:2545px">Phone*</div>
  <div class="field" style="top:2600px">Email*</div>
  <div class="field" style="top:2657px;height:123px">Message</div>
  <div class="btn" style="left:121px;top:2807px;width:154px;height:33px;font-weight:400">Submit</div>

  <h2 class="abs display section-h" style="left:615px;top:2386px;font-weight:400">MAP</h2>
  <div class="abs map" role="img" aria-label="Street map showing the office location with a red pin"></div>
</section>

<footer class="footer">
  <h5 style="left:121px">SUBSCRIBE</h5>
  <p class="abs" style="left:121px;top:128px;width:230px;line-height:22px">Get the latest updates and offer Lorem Ipsum is simply dummy text of the printing.</p>
  <div class="abs sub-field">Enter Your Email</div>
  <div class="abs sub-btn"><svg width="16" height="12" viewBox="0 0 16 12"><rect x="1" y="1" width="14" height="10" fill="none" stroke="#fff" stroke-width="1.5"/><path d="M1 1l7 6 7-6" fill="none" stroke="#fff" stroke-width="1.5"/></svg></div>

  <h5 style="left:402px">QUICK LINKS</h5>
  <ul class="abs" style="left:402px;top:128px">
    <li>›&nbsp; Home</li><li>›&nbsp; About us</li><li>›&nbsp; Services</li><li>›&nbsp; Blogs</li><li>›&nbsp; Testimonials</li><li>›&nbsp; Contact us</li>
  </ul>

  <h5 style="left:631px">OFFICE</h5>
  <ul class="abs" style="left:596px;top:128px">
    <li><svg width="12" height="14" viewBox="0 0 12 14"><path d="M6 0a5 5 0 0 1 5 5c0 4-5 9-5 9S1 9 1 5a5 5 0 0 1 5-5z" fill="#ddd"/><circle cx="6" cy="5" r="2" fill="#232323"/></svg><span style="margin-left:14px">Daniel Morwa Ltd</span></li>
    <li style="padding-left:36px">1234 Riverside Road West</li>
    <li style="padding-left:36px">Maun, NG 12345</li>
    <li><svg width="12" height="12" viewBox="0 0 12 12"><path d="M2 0l3 3-1.5 2a7 7 0 0 0 3.5 3.5L9 7l3 3-2 2C5 12 0 7 0 2z" fill="#ddd"/></svg><span style="margin-left:14px">+123 456 7890</span></li>
    <li><svg width="12" height="10" viewBox="0 0 12 10"><rect width="12" height="10" fill="#ddd"/><path d="M0 0l6 5 6-5" fill="none" stroke="#232323"/></svg><span style="margin-left:14px">info@kpv.construction</span></li>
    <li><svg width="12" height="12" viewBox="0 0 12 12"><circle cx="6" cy="6" r="6" fill="#ddd"/><path d="M6 2.5V6h3" fill="none" stroke="#232323" stroke-width="1.4"/></svg><span style="margin-left:14px">Mon-Sat 9:00am-6 :00pm</span></li>
  </ul>

  <div class="abs" style="left:861px;top:80px;font-weight:700;font-size:14px;color:var(--white);letter-spacing:1px">KPV CONSTRUCTION</div>
  <p class="abs" style="left:861px;top:160px;width:230px;line-height:20px">Lorem Ipsum is simply dummy text the printing and typesetting industry. Lorem Ipsum hasbeen the industry standard.</p>
  <div class="abs" style="left:861px;top:246px;display:flex;align-items:center;gap:6px">Read More <svg width="14" height="14" viewBox="0 0 14 14"><circle cx="7" cy="7" r="6" fill="none" stroke="#ddd" stroke-width="1.3"/><path d="M6 4.5l2.5 2.5L6 9.5" fill="none" stroke="#ddd" stroke-width="1.3"/></svg></div>
</footer>

<div class="bar">
  <span class="abs" style="left:121px;top:21px">© Copyright 2019 Construction. All Rights Reserved</span>
  <svg class="abs" style="left:934px;top:17px" width="150" height="26" viewBox="0 0 150 26">
    <circle cx="13" cy="13" r="12" fill="#fff"/><circle cx="50" cy="13" r="12" fill="#fff"/><circle cx="87" cy="13" r="12" fill="#fff"/><circle cx="124" cy="13" r="12" fill="#fff"/>
  </svg>
</div>

</body>
</html>
```